PREMIUM AGENCY High End Business Card - A+++ Designers Wanted

** DO NOT ATTEMPT TO CONTACT ME THROUGH SEARCHING ON ZINTREL OR EMAILING ME THROUGH MY WEBSITE **

I need a fresh, contemporary business card designed using the logo attached (BRONSALK)

I have attached the font for BRONSALK

It must have a premium look and feel. The business card size must be STANDARD size.

You can submit either/both VERTICAL or HORIZONTAL designs.

FRONT: It must have the following sample information on

Paul Ardley
Director Operations
Mobile +61 452 118 906
Email paulardley@bronsalk.com
www.bronsalk.com

The REAR of the business card must have the words

CREATE INSPIRE TOMORROW

as part of the design, in the same font (NEXA) attached.

The words do not need to be in capitals, or on the same line, please design this as you see it best working.

ADDITIONAL INFORMATION
======================

The BRONSALK logo must be on the front of the card

I want Ultraviolet printing on the final design, to enhance either the NAME of the person OR the BRONSALK logo OR the words on the back of the card.

Target Market(s)

Agency, Advertising Agency, Creative, Designers

Industry/Entity Type

Media

Contact Information for Business Card

Design Agency, Contemporary, Premium look and feel, High Quality

Font styles to use
Serif
Sans Serif
Other font styles liked:
• ATTACHED TO PROJECT

Requirements
Must have
• BLACK & WHITE as the primary design, and if you feel there can be a highlighted colour, then this can be used.
• The Logo ICON attached is blue, this colour must not be changed.
• I have attached the partner brand BRONSALK MEDIA incase you need to manipulate the original files.
• ** DO NOT ATTEMPT TO CONTACT ME THROUGH SEARCHING ON ZINTREL OR EMAILING ME THROUGH MY WEBSITE **
Nice to have
• Must be Premium. I have attached some sample designs, that I like that would be a good inspiration for where this can be taken.
• My favourite design is is the KESTRAVUE2-BUSINESSCARD-TEMPLATE
Should not have
• No funny or silly standard / off the shelf designs

```html
<!DOCTYPE html>
<html lang="en">
<head>
<meta charset="utf-8">
<title>Paul Ardley – Business Card</title>
<link rel="stylesheet" href="https://fonts.googleapis.com/css2?family=Montserrat:wght@300;600;700&family=EB+Garamond:wght@700&display=swap">
<style>
  :root {
    --ink: #1b1a1f;
    --brand-blue: #3aa8dc;
    --paper: #f2f2f2;
  }
  * { margin: 0; padding: 0; box-sizing: border-box; }
  html, body { width: 791px; height: 1200px; overflow: hidden; background: var(--ink); }
  .card {
    position: relative;
    width: 791px;
    height: 1200px;
    background: var(--ink);
    color: var(--paper);
    font-family: "Montserrat", sans-serif;
  }
  .name {
    position: absolute;
    left: 78px;
    top: 62px;
    font-size: 90px;
    font-weight: 700;
    letter-spacing: -1px;
    line-height: 1;
  }
  .name .first { color: var(--brand-blue); }
  .role {
    position: absolute;
    left: 79px;
    top: 168px;
    font-size: 53px;
    font-weight: 300;
    line-height: 1;
  }
  .contact-heading {
    position: absolute;
    left: 80px;
    top: 436px;
    font-size: 44px;
    font-weight: 600;
    color: var(--brand-blue);
    letter-spacing: -0.5px;
    line-height: 1;
  }
  .contact-heading .bar { color: var(--paper); font-weight: 600; }
  .contact-heading .bar:first-child { margin-right: 14px; }
  .contact-heading .bar:last-child { margin-left: 14px; }
  .contact-line {
    position: absolute;
    display: flex;
    align-items: center;
    font-family: "EB Garamond", serif;
    font-weight: 700;
    font-size: 36px;
    line-height: 1;
  }
  .contact-line svg { flex: none; }
  .phone { left: 80px; top: 548px; }
  .phone svg { margin-right: 20px; }
  .email { left: 80px; top: 650px; }
  .email svg { margin-right: 22px; }
  .website {
    position: absolute;
    left: 87px;
    top: 842px;
    font-family: "EB Garamond", serif;
    font-weight: 700;
    font-size: 33px;
    line-height: 1;
  }
  .brand-band {
    position: absolute;
    left: 0;
    top: 963px;
    width: 791px;
    height: 237px;
    background: var(--brand-blue);
    display: flex;
    align-items: center;
    justify-content: center;
    gap: 18px;
  }
  .brand-mark {
    width: 34px;
    height: 34px;
    border: 4px solid var(--paper);
    border-radius: 50%;
  }
  .brand-name {
    color: var(--paper);
    font-family: "Montserrat", sans-serif;
    font-weight: 600;
    font-size: 44px;
    letter-spacing: 4px;
    line-height: 1;
  }
</style>
</head>
<body>
<main class="card">
  <h1 class="name"><span class="first">Paul</span> Ardley</h1>
  <p class="role">Director Operations</p>

  <h2 class="contact-heading"><span class="bar">|</span>Get In Touch<span class="bar">|</span></h2>

  <p class="contact-line phone">
    <svg width="52" height="50" viewBox="0 0 52 50" fill="none" stroke="#f2f2f2" stroke-width="2.4" stroke-linejoin="round" aria-hidden="true">
      <path d="M8 6 L16 4 L22 16 L17 20 C20 28 25 33 32 36 L36 31 L48 37 L46 45 C30 48 6 26 8 6 Z"/>
      <path d="M28 10 A12 12 0 0 1 40 22"/>
      <path d="M28 3 A19 19 0 0 1 47 22"/>
    </svg>
    +61 452 118 906
  </p>

  <p class="contact-line email">
    <svg width="52" height="36" viewBox="0 0 52 36" fill="none" stroke="#f2f2f2" stroke-width="2.6" stroke-linejoin="round" aria-hidden="true">
      <rect x="2" y="2" width="48" height="32"/>
      <path d="M2 2 L26 22 L50 2"/>
      <path d="M2 34 L20 17 M50 34 L32 17"/>
    </svg>
    paulardley@bronsalk.com
  </p>

  <p class="website">www.bronsalk.com</p>

  <footer class="brand-band">
    <span class="brand-mark" aria-hidden="true"></span>
    <span class="brand-name">BRONSALK MEDIA</span>
  </footer>
</main>
</body>
</html>
```